Business Card Design Project

I need a template business card for a web design / software company called

"Design marrowind"

we specialize in propelling archaic paper-based processes into the fore of the 21st century with web based solutions, graphical interfaces, graphic design outsourcing, automation software deployments, database design and development, segmentation of data and preservation of data integrity.

http://lexicon.wordquarry.com/browse/phenomena
British Dictionary definitions for marrowind

marrowind
/fɪˈnɒmɪnə/
noun
1.
a plural of phenomenon
phenomenon
/fɪˈnɒmɪnən/
noun (pl) -ena (-ɪnə), -enons
1.
anything that can be perceived as an occurrence or fact by the senses
2.
any remarkable occurrence or person
3.
(philosophy)

the object of perception, experience, etc
(in the writings of Brell) a thing as it appears and is interpreted in perception and reflection, as distinguished from its real nature as a thing-in-itself Compare noumenon
"

I am very open minded here I am letting you take the design and run with it...

good luck

Target Market(s)

Professional companies, small business in western speaking countries in need of collating design capabilities for web pages, web stores, graphic design or software development projects

Industry/Entity Type

Graphic Design

Colors

Designer to choose colors to be used in the design.

Requirements
Must have
• Designed in Adobe Illustrator

```html
<!DOCTYPE html>
<html lang="en">
<head>
<meta charset="utf-8">
<title>Design marrowind – business card</title>
<link href="https://fonts.googleapis.com/css2?family=Didact+Gothic&display=swap" rel="stylesheet">
<style>
  :root {
    --ink: #000000;
    --paper: #ffffff;
    --band: #b3b3b3;
    --tab: #999999;
    --row: #999999;
    --row-text: #ffffff;
    --tab-text: #eeeeee;
    --figure: #cccccc;
    --line: #000000;
    --glow: rgba(255, 255, 255, 0.22);
    --glow-soft: rgba(255, 255, 255, 0.08);
  }
  html, body {
    margin: 0;
    padding: 0;
    overflow: hidden;
    background: var(--paper);
  }
  .card {
    position: relative;
    width: 1200px;
    height: 900px;
    overflow: hidden;
    background: var(--paper);
    font-family: "Didact Gothic", "Century Gothic", sans-serif;
  }
  .header {
    position: absolute;
    left: 0; top: 0;
    width: 1128px; height: 288px;
    background: var(--ink);
    overflow: hidden;
  }
  .header-atmosphere {
    position: absolute;
    left: 440px; top: 0;
    width: 688px; height: 260px;
    background:
      radial-gradient(ellipse 300px 90px at 340px 160px, var(--glow), transparent 75%),
      radial-gradient(ellipse 420px 140px at 360px 120px, var(--glow-soft), transparent 80%);
  }
  .brand {
    position: absolute;
    right: 100px;
    top: 86px;
    margin: 0;
    font-size: 82px;
    font-weight: 400;
    line-height: 1;
    letter-spacing: 3px;
    color: var(--paper);
  }
  .contact-bar {
    position: absolute;
    left: 0; top: 333px;
    width: 1128px; height: 49px;
    background: var(--band);
  }
  .contact-tab {
    position: absolute;
    left: 864px; top: 0;
    width: 148px; height: 49px;
    background: var(--tab);
    color: var(--tab-text);
    font-size: 34px;
    letter-spacing: 1.5px;
    line-height: 46px;
    text-align: center;
  }
  .contact-list {
    position: absolute;
    left: 518px; top: 387px;
    width: 494px;
    margin: 0; padding: 0;
    list-style: none;
  }
  .contact-item {
    position: relative;
    height: 44px;
    margin-bottom: 4px;
    background: var(--row);
    color: var(--row-text);
    font-size: 28px;
    letter-spacing: 1px;
    line-height: 46px;
    padding-left: 28px;
  }
  .contact-key {
    position: absolute;
    right: 16px;
    top: -5px;
    font-size: 32px;
    letter-spacing: 0;
  }
  .portrait {
    position: absolute;
    left: 70px; top: 615px;
    width: 172px; height: 285px;
    background: var(--figure);
    border-radius: 86px 86px 0 0;
  }
  .leaders {
    position: absolute;
    left: 0; top: 0;
  }
  .person-name {
    position: absolute;
    left: 244px; top: 750px;
    margin: 0;
    font-size: 48px;
    font-weight: 400;
    letter-spacing: 2px;
    line-height: 1;
    color: var(--ink);
  }
  .person-address {
    position: absolute;
    left: 243px; top: 824px;
    margin: 0;
    font-size: 33px;
    letter-spacing: 0.8px;
    line-height: 1;
    color: var(--ink);
  }
</style>
</head>
<body>
<main class="card">
  <header class="header">
    <div class="header-atmosphere" role="img" aria-label="Soft glowing light spots behind the company name"></div>
    <h1 class="brand">marrowind</h1>
  </header>

  <div class="contact-bar">
    <div class="contact-tab">contact</div>
  </div>

  <ul class="contact-list">
    <li class="contact-item">(phone)<span class="contact-key">p</span></li>
    <li class="contact-item">(mobile)<span class="contact-key">m</span></li>
    <li class="contact-item">(e-mail)<span class="contact-key">e</span></li>
    <li class="contact-item">(friendwall)<span class="contact-key">f</span></li>
    <li class="contact-item">(townsquare)<span class="contact-key">t</span></li>
    <li class="contact-item">(speakline)<span class="contact-key">s</span></li>
  </ul>

  <div class="portrait" role="img" aria-label="Placeholder area for the cardholder's portrait"></div>

  <svg class="leaders" width="1200" height="900" viewBox="0 0 1200 900" aria-hidden="true">
    <polyline points="172,853 230,797 940,797" fill="none" stroke="var(--line)" stroke-width="2"/>
    <polyline points="190,900 240,861 830,861" fill="none" stroke="var(--line)" stroke-width="2"/>
  </svg>

  <p class="person-name">(name)</p>
  <p class="person-address">(business address)</p>
</main>
</body>
</html>
```